Ward Compass Business Card Design*

We need a business card design for our company Ward Compass. Our company is specialized in providing online consulting services regarding medical institutions, hospitals and doctors. We work with patients worldwide looking to choose between healthcare providers. We have a website you may use as a reference, where we list doctors and clinics worldwide. So we target Medical providers as well as patients worldwide.
Target Market(s)
Medical Providers and patients around the world
Industry/Entity Type
Medical
Contact Information for Business Card
Salma Driouch
CEO
+90 612 348 2751
info@wardcompass.example
www.wardcompass.example
17 Essafsaf 3 H.Q.L. Rabat, Morocco
Requirements
Must have
- Company logo/name on one full side, personal info and smaller logo and company name on the other side.
Nice to have
- Smart and elegant design

```html
<!DOCTYPE html>
<html lang="en">
<head>
<meta charset="utf-8">
<title>Ward Compass Business Card</title>
<link rel="stylesheet" href="https://fonts.googleapis.com/css2?family=Montserrat:wght@300;700;800&family=Roboto:wght@300;400&display=swap">
<style>
  :root {
    --navy: #173a6a;
    --grey: #8a8a8a;
    --ink: #4a4a4a;
    --paper: #ffffff;
    --backdrop: #ececee;
  }
  * { margin: 0; padding: 0; box-sizing: border-box; }
  html, body { width: 1200px; height: 900px; overflow: hidden; }
  body {
    background: var(--backdrop);
    font-family: "Roboto", Arial, sans-serif;
    position: relative;
  }
  .card {
    position: absolute;
    top: 296px;
    width: 540px;
    height: 308px;
    background: var(--paper);
    box-shadow: 0 2px 10px rgba(0,0,0,0.08);
    overflow: hidden;
  }
  .card--front { left: 40px; }
  .card--back { left: 620px; }

  .brand {
    display: flex;
    align-items: center;
    gap: 12px;
    font-family: "Montserrat", Arial, sans-serif;
    font-weight: 700;
    color: var(--navy);
    letter-spacing: 1px;
    text-transform: uppercase;
    white-space: nowrap;
  }
  .brand__dot {
    border-radius: 50%;
    background: var(--navy);
    flex: none;
  }

  .card--front .brand {
    position: absolute;
    left: 0; right: 0; top: 112px;
    justify-content: center;
    font-size: 34px;
  }
  .card--front .brand__dot { width: 30px; height: 30px; }
  .front__url {
    position: absolute;
    left: 0; right: 0; top: 210px;
    text-align: center;
    font-family: "Montserrat", Arial, sans-serif;
    font-weight: 300;
    font-size: 15px;
    letter-spacing: 6px;
    color: var(--ink);
  }

  .card--back .brand {
    position: absolute;
    left: 40px; top: 78px;
    font-size: 22px;
    gap: 9px;
  }
  .card--back .brand__dot { width: 20px; height: 20px; }

  .person {
    position: absolute;
    left: 40px; top: 138px;
    text-align: right;
    width: 230px;
    font-family: "Montserrat", Arial, sans-serif;
  }
  .person__name { font-weight: 800; font-size: 24px; line-height: 1.1; }
  .person__first { color: var(--navy); }
  .person__last { color: var(--grey); }
  .person__role {
    font-weight: 300;
    font-size: 15px;
    color: var(--navy);
    letter-spacing: 1px;
    margin-top: 3px;
  }

  .divider {
    position: absolute;
    left: 288px; top: 128px;
    width: 2px; height: 72px;
    background: var(--navy);
  }

  .contacts {
    position: absolute;
    left: 302px; top: 130px;
    list-style: none;
    font-size: 12.5px;
    color: var(--ink);
  }
  .contacts li {
    display: flex;
    align-items: center;
    gap: 8px;
    height: 22px;
  }
  .contacts svg { width: 14px; height: 14px; flex: none; }

  .address-band {
    position: absolute;
    left: 0; right: 0; bottom: 26px;
    height: 30px;
    background: var(--navy);
    color: var(--paper);
    font-size: 12.5px;
    letter-spacing: 0.3px;
    display: flex;
    align-items: center;
    justify-content: center;
  }
</style>
</head>
<body>

  <section class="card card--front" aria-label="Business card, front">
    <div class="brand"><span class="brand__dot"></span>Ward Compass</div>
    <p class="front__url">www.wardcompass.example</p>
  </section>

  <section class="card card--back" aria-label="Business card, back">
    <div class="brand"><span class="brand__dot"></span>Ward Compass</div>

    <div class="person">
      <p class="person__name"><span class="person__first">Salma</span> <span class="person__last">Driouch</span></p>
      <p class="person__role">CEO</p>
    </div>

    <div class="divider"></div>

    <ul class="contacts">
      <li>
        <svg viewBox="0 0 16 16" aria-hidden="true"><path fill="#173a6a" d="M3.2 1.5l2.3-.4 1.2 3-1.5 1.1a8 8 0 0 0 4.6 4.6l1.1-1.5 3 1.2-.4 2.3c-.2.8-.9 1.3-1.7 1.2C6.6 12.5 3.5 9.4 2 4.2c-.1-.8.4-1.5 1.2-2.7z"/></svg>
        +90 612 348 2751
      </li>
      <li>
        <svg viewBox="0 0 16 16" aria-hidden="true"><rect x="1" y="3" width="14" height="10" fill="#173a6a"/><path d="M1.5 3.5 8 9l6.5-5.5" fill="none" stroke="#fff" stroke-width="1.2"/></svg>
        info@wardcompass.example
      </li>
      <li>
        <svg viewBox="0 0 16 16" aria-hidden="true"><circle cx="8" cy="8" r="6.5" fill="none" stroke="#173a6a" stroke-width="1.4"/><ellipse cx="8" cy="8" rx="2.8" ry="6.5" fill="none" stroke="#173a6a" stroke-width="1.1"/><path d="M1.5 8h13" stroke="#173a6a" stroke-width="1.1"/></svg>
        www.wardcompass.example
      </li>
    </ul>

    <div class="address-band">17 Essafsaf 3 H.Q.L. Rabat, Morocco</div>
  </section>

</body>
</html>
```